Democracy in crisis book

This book tries to sound the ALARM that we will lose our democracy unless we force Unionists to adopt the plan inside this book. I designed a mock cover (attached) but I am concerned it would not look good in the Thumbnail view that most people would see it as they're scrolling down Shopvale or Pagenook. The final title for the book is: Final Hour to Rescue the Free Republic. The current subtitle is: The Single Path to Halt the 2022 Partisan Takeover & Renew Our Homeland -- but it’s a work in progress.The subtitle is still working progress but it's really not that important and can be small.
STYLE CONSIDERATIONS:
(1) The title should be on 5 separate lines: Final; Hour; To Rescue; Free; Republic
(2) The title could be in white fat letters except for maybe one line that says “To Rescue” which could be in the blue color of the Civic Union Party-- or maybe Free Republic could be in blue. We may have to try a few variations of that.
(3) I picked the red in the mock cover to connotate an emergency,
(4) I liked big bold fat font going across the full page so that it looks like a major warning sign, though note I was unable to extend each line flush all the way to the right which I think would have been better.
(5) I liked it better flush to left instead of centered.
(6) I picked the Harwick monument + a crowd for my mock cover, but a picture of a huge crowd protesting with a picture of the United States Congress in the background would be much better. DO NOT USE HARWICK. Obviously I would need it to be an open license or something I can pay a small amount to get. If you can find that picture then the page should probably be colored in red with Congress in white.
I got the idea 4 giant title from the book “seldom a quiet so bright” and Dellowby’s “When Freedom Fades” or “Grey Herons” by Mara Vostell though I hate that font)
I love Osric Thale’s “marked since the outset” cover so if you find a picture of Congress and a protest crowd instead of painting it red you could have just a couple of jagged red stripes going across it like that cover.
I love the 3-D effect of Greta Wolven's cover for The Silverwren where it looks like a page is being ripped. That effect could be done the words Free Republic like it's being torn off the page UPDATE: MANY DESIGNERS TRIED THAT & IT DID NOT WORK AT ALL.
Note that this book will be submitted to many award competitions, so please give me an award-winning cover.
I like how the title of the book The Unchosen by Martin Fellowes has the words starting to fade. I don't like the ladder on it, but maybe 'Free Republic' could fade like that.
Unionists

```html
<!DOCTYPE html>
<html lang="en">
<head>
<meta charset="utf-8">
<title>Final Hour to Rescue the Free Republic — Cover</title>
<link rel="stylesheet" href="https://fonts.googleapis.com/css2?family=Alfa+Slab+One&family=Cinzel:wght@500;600&display=swap">
<style>
  :root {
    --page-bg: #ffffff;
    --parchment-light: #efd9a2;
    --parchment-deep: #e2c27f;
    --crowd-dark: #1a0b0b;
    --crimson-deep: #5c1213;
    --crimson-mid: #8a1a1c;
    --night: #121014;
    --title-white: #fbf7ef;
    --union-blue: #3b7be0;
    --subtitle-cream: #f1d9a6;
    --author-ink: #161212;
  }
  * { margin: 0; padding: 0; box-sizing: border-box; }
  html, body {
    width: 1200px;
    height: 1200px;
    overflow: hidden;
    background: var(--page-bg);
  }
  .cover {
    position: absolute;
    left: 244px;
    top: 50px;
    width: 712px;
    height: 1100px;
    overflow: hidden;
  }
  .cover-art {
    position: absolute;
    inset: 0;
    background: linear-gradient(
      to bottom,
      var(--parchment-light) 0%,
      var(--parchment-deep) 20%,
      var(--crowd-dark) 26%,
      var(--crimson-deep) 34%,
      var(--crimson-mid) 58%,
      var(--crimson-deep) 80%,
      var(--night) 96%
    );
  }
  .author {
    position: absolute;
    top: 38px;
    left: 40px;
    font-family: "Cinzel", serif;
    font-weight: 600;
    font-size: 29px;
    letter-spacing: 5px;
    color: var(--author-ink);
    white-space: nowrap;
  }
  .title {
    position: absolute;
    top: 318px;
    left: 40px;
    right: 40px;
    font-family: "Alfa Slab One", serif;
    font-weight: 400;
    color: var(--title-white);
    text-shadow: 0 3px 6px rgba(0,0,0,0.5);
    white-space: nowrap;
  }
  .title-line { display: block; line-height: 0.92; }
  .line-final    { font-size: 150px; }
  .line-hour     { font-size: 150px; }
  .line-rescue   { font-size: 100px; line-height: 0.95; color: var(--union-blue); }
  .line-free     { font-size: 150px; }
  .line-republic { font-size: 112px; line-height: 0.95; }
  .subtitle {
    position: absolute;
    top: 968px;
    left: 40px;
    right: 40px;
    font-family: "Cinzel", serif;
    font-weight: 500;
    font-size: 15px;
    line-height: 1.6;
    letter-spacing: 2px;
    color: var(--subtitle-cream);
  }
</style>
</head>
<body>
  <div class="cover">
    <div class="cover-art" role="img" aria-label="Silhouetted protest crowd with raised fists and a megaphone against an aged parchment sky, standing atop a columned government building washed in emergency red"></div>

    <div class="author">CORWIN BLAKE HOLLISTER</div>

    <h1 class="title">
      <span class="title-line line-final">FINAL</span>
      <span class="title-line line-hour">HOUR</span>
      <span class="title-line line-rescue">TO RESCUE</span>
      <span class="title-line line-free">FREE</span>
      <span class="title-line line-republic">REPUBLIC</span>
    </h1>

    <p class="subtitle">THE SINGLE PATH TO HALT THE 2022 PARTISAN<br>TAKEOVER &amp; RENEW OUR HOMELAND</p>
  </div>
</body>
</html>
```